CORPORATE AND CLASSY CHRISTMAS CARD (CONTEST)

We want a Christmas card for wealth managers to issue to high net worth clients. Very classy (the target market is clients with investments - typically more than £100,000 which is why the card needs to be very classy). Very corporate. The finished printed card will be a5 to fit existing envelopes. The design will also be used as part of a digital card so i need the image in a format for email as well as print. The brand uses a silver (foil block) on its logo and a specific pan tone ref olive green (reference 620). Not too religious and include a quirky message.

Target Market(s)

High net worth clients - clients with investments, typically more than £100,000 which is why the card needs to be very classy

Requirements
Must have
• The image in a format for email as well as print.
Nice to have
• Very corporate, very classy, the colour scheme of the brand - silver (foil block) and a specific pan ton ref olive green (ref 620) used in a quirky and different way
Should not have
• not too religious

```html
<!DOCTYPE html>
<html lang="en">
<head>
<meta charset="utf-8">
<title>Christmas Card</title>
<link rel="stylesheet" href="https://fonts.googleapis.com/css2?family=Alegreya:wght@400;500&display=swap">
<style>
  :root {
    --olive: #827631;
    --olive-text: #7f742c;
    --silver-light: #f1f1f1;
    --silver-mid: #d9d9d9;
    --silver-dark: #bdbdbd;
  }
  * { margin: 0; padding: 0; box-sizing: border-box; }
  html, body {
    width: 1200px;
    height: 878px;
    overflow: hidden;
    background: #ffffff;
  }
  .card {
    position: relative;
    width: 1200px;
    height: 878px;
    display: flex;
    font-family: "Alegreya", Georgia, serif;
  }
  .card__cover {
    position: relative;
    width: 532px;
    height: 100%;
    background: var(--olive);
  }
  .card__tree {
    position: absolute;
    left: 82px;
    top: 146px;
    width: 376px;
    height: 532px;
    background: linear-gradient(160deg, var(--silver-mid), var(--silver-dark));
    box-shadow: inset 4px 6px 10px rgba(0,0,0,0.25);
  }
  .card__inside {
    position: relative;
    flex: 1;
    height: 100%;
    background: linear-gradient(160deg, var(--silver-light) 0%, #e6e6e6 45%, var(--silver-dark) 100%);
    box-shadow: inset 10px 0 14px -8px rgba(0,0,0,0.35);
    color: var(--olive-text);
    text-align: center;
  }
  .card__message {
    position: absolute;
    top: 144px;
    left: 0;
    right: 0;
    font-size: 26px;
    line-height: 39px;
    padding-left: 8px;
  }
  .card__greeting {
    position: absolute;
    top: 402px;
    left: 0;
    right: 0;
    font-size: 36px;
    font-weight: 500;
    padding-left: 8px;
  }
  .card__sender {
    position: absolute;
    top: 772px;
    left: 0;
    right: 0;
    font-size: 26px;
    letter-spacing: 6px;
    text-transform: uppercase;
    padding-left: 8px;
  }
</style>
</head>
<body>
  <main class="card">
    <section class="card__cover">
      <div class="card__tree" role="img" aria-label="Christmas tree with star, cut out of the olive cover to reveal silver beneath"></div>
    </section>
    <section class="card__inside">
      <p class="card__message">
        At this time of the year we stop and think<br>
        of the people that are special to us.<br>
        We are greatful to have you at our side.
      </p>
      <p class="card__greeting">Merry Christmas!</p>
      <p class="card__sender">Halden Group</p>
    </section>
  </main>
</body>
</html>
```